Business card design and logo for plumbing bussiness

We are wanting a logo for a plumbing business is Queensland Australia. KRV Plumbing and Drainage will be doing works on domestic and commercial sites.
Plumbing, drainage and gas works. We are wanting something that will stand out and be noticed. Colours could be black blue and white but open for suggestions.

Target Market(s)

Builders and home renovators

Industry/Entity Type

Plumbing

Contact Information for Business Card

Miles Dorgan - Director
0417 582 913
miles@krvplumbing.example.com.au
QBCC: 847 2106
ABN: 52 319 407 281

Font styles to use
Sans Serif

Colors
000000

Requirements
Must have
• Clear defined branding

```html
<!DOCTYPE html>
<html lang="en">
<head>
<meta charset="utf-8">
<title>KRV Plumbing and Drainage – Business Card</title>
<link rel="stylesheet" href="https://fonts.googleapis.com/css2?family=Montserrat:wght@600;700&display=swap">
<style>
  :root {
    --ink: #000000;
    --glow: #12251f;
    --glow-soft: #0a1512;
    --paper: #ffffff;
    --brand-faint: #2c3935;
  }
  html, body {
    margin: 0;
    padding: 0;
    width: 1200px;
    height: 720px;
    overflow: hidden;
    background: var(--ink);
  }
  .card {
    position: relative;
    width: 1200px;
    height: 720px;
    overflow: hidden;
    font-family: "Montserrat", sans-serif;
    color: var(--paper);
    background:
      radial-gradient(ellipse 420px 360px at 610px 330px, var(--glow) 0%, var(--glow-soft) 45%, var(--ink) 100%);
  }
  .brand-mark {
    position: absolute;
    left: 310px;
    top: 300px;
    width: 600px;
    text-align: center;
    font-weight: 700;
    font-size: 38px;
    line-height: 1;
    letter-spacing: 1px;
    color: var(--brand-faint);
    text-transform: uppercase;
    white-space: nowrap;
  }
  .identity {
    position: absolute;
    left: 80px;
    top: 91px;
    height: 104px;
    padding-left: 30px;
    border-left: 7px solid var(--paper);
  }
  .identity__name {
    margin: 0;
    font-weight: 700;
    font-size: 40px;
    line-height: 1;
    letter-spacing: 0.5px;
    padding-top: 4px;
  }
  .identity__role {
    margin: 28px 0 0;
    font-weight: 600;
    font-size: 31px;
    line-height: 1;
  }
  .contact {
    position: absolute;
    right: 88px;
    top: 429px;
    height: 191px;
    border-right: 11px solid var(--paper);
    padding-right: 18px;
  }
  .contact__row {
    display: flex;
    align-items: center;
    justify-content: flex-end;
    font-weight: 600;
    white-space: nowrap;
  }
  .contact__text {
    text-align: right;
    line-height: 1.25;
  }
  .contact__email { font-size: 32px; height: 56px; }
  .contact__phone { font-size: 33px; height: 60px; }
  .contact__legal { font-size: 33px; }
  .contact__icon {
    width: 50px;
    height: 50px;
    margin-left: 24px;
    flex: none;
  }
</style>
</head>
<body>
  <main class="card">
    <div class="brand-mark">KRV Plumbing and Drainage</div>

    <header class="identity">
      <h1 class="identity__name">MILES DORGAN</h1>
      <p class="identity__role">DIRECTOR</p>
    </header>

    <section class="contact">
      <div class="contact__row contact__email">
        <span class="contact__text">miles@krvplumbing.example.com.au</span>
        <svg class="contact__icon" viewBox="0 0 50 50" aria-hidden="true" fill="none" stroke="#fff" stroke-width="2.4">
          <circle cx="25" cy="25" r="22"/>
          <ellipse cx="25" cy="25" rx="10" ry="22"/>
          <line x1="25" y1="3" x2="25" y2="47"/>
          <line x1="3" y1="25" x2="47" y2="25"/>
          <path d="M7 13 H43 M7 37 H43"/>
        </svg>
      </div>
      <div class="contact__row contact__phone">
        <span class="contact__text">0417 582 913</span>
        <svg class="contact__icon" viewBox="0 0 50 50" aria-hidden="true" fill="#fff">
          <path d="M6 16 C6 8 44 8 44 16 L44 20 L35 20 L35 15 L15 15 L15 20 L6 20 Z"/>
          <path d="M16 19 L34 19 L43 36 L43 44 L7 44 L7 36 Z"/>
          <circle cx="25" cy="32" r="6" fill="#000"/>
          <circle cx="25" cy="32" r="2.5"/>
        </svg>
      </div>
      <div class="contact__row contact__legal">
        <span class="contact__text">QBCC: 847 2106<br>ABN: 52 319 407 281</span>
        <svg class="contact__icon" viewBox="0 0 50 58" aria-hidden="true" fill="none" stroke="#fff" stroke-width="2.4" style="height:58px">
          <path d="M3 24 L25 5 L47 24"/>
          <path d="M9 20 V55 H41 V20"/>
          <rect x="14" y="27" width="8" height="8"/>
          <rect x="28" y="27" width="8" height="8"/>
          <path d="M20 55 V42 H30 V55"/>
          <line x1="9" y1="38" x2="41" y2="38"/>
        </svg>
      </div>
    </section>
  </main>
</body>
</html>
```